Custom Cabinet Shop Needs a website design

Hi,
We need a website for a Custom Cabinet Shop and Cabinet parts manufacturing business.
The business has two sides to it. One side provides custom Kitchens, vanities, entertainment units, offices and what not to homeowners and contractors.
The 2nd side of the business provides built to order cabinet boxes and other parts required to put together a project to other cabinet shops, small contractors looking to install there own cabinets.
Website will need a Gallery to display work.
Color scheme to go well with logo.
current website is www.brindlemoorcustomcabinets.com
being changed to www.brindlemoor.ca
Tagline "Joinery with Spirit"
Mission Statement "Our passion is to deliver inspired cabinetry solutions to suit all your needs, supported by our phenomenal star class customer service"
The website should convey quality and professionalism.
Thank you.
Target Market(s)
Homeowners/ Contractors
Industry/Entity Type
Entertainment
Coding
Coded - Design and coding required
Number of Pages Required
1 page
Look and feel
Each slider illustrates characteristics of the customer's brand and the style your logo design should communicate.

```html
<!DOCTYPE html>
<html lang="en">
<head>
<meta charset="utf-8">
<title>Brindlemoor Custom Cabinets</title>
<link href="https://fonts.googleapis.com/css2?family=Open+Sans:wght@400;600;700&display=swap" rel="stylesheet">
<style>
:root{
  --wood:#b9753f;
  --wood-dark:#8a5226;
  --wood-light:#d49a63;
  --ink:#333;
  --muted:#777;
  --line:#e2e2e2;
  --footer:#4b4b4b;
  --footer-deep:#3c3c3c;
  --footer-text:#cfcfcf;
  --paper:#fff;
  --star:#e3a21a;
}
*{box-sizing:border-box;margin:0;padding:0}
html,body{width:1200px;height:2428px;overflow:hidden;background:var(--paper)}
body{font-family:"Open Sans",Arial,sans-serif;color:var(--ink);position:relative}
.abs{position:absolute}

/* header */
.brand{left:180px;top:44px;display:flex;align-items:center;gap:12px}
.brand-mark{width:34px;height:34px;border-radius:50%;background:var(--wood)}
.brand-name{font-size:30px;font-weight:700;letter-spacing:1px;color:#222;line-height:1}
.brand-tag{font-size:12px;color:var(--muted);margin-top:4px;letter-spacing:.5px}
.nav-shelf{left:600px;top:100px;width:400px;height:8px;background:var(--wood);border-radius:2px}
.nav{left:620px;top:40px;display:flex;gap:14px}
.nav a{display:flex;align-items:center;justify-content:center;width:58px;height:58px;border:1px solid #bbb;background:#fafafa;font-size:10px;color:#555;text-decoration:none;text-transform:uppercase;position:relative}
.nav a::before{content:"";position:absolute;top:-26px;left:50%;width:1px;height:26px;background:#bbb}

/* hero */
.hero-frame{left:172px;top:150px;width:856px;height:276px;background:var(--wood);border-radius:4px;box-shadow:0 6px 0 var(--wood-dark)}
.hero-photo{left:190px;top:166px;width:820px;height:244px;background:linear-gradient(120deg,#f3efe9,#d9d2c6 55%,#a58d73)}
.hero-form{left:760px;top:190px;width:230px;height:200px;background:rgba(185,117,63,.88);padding:14px}
.hero-form .field{height:22px;background:#fff;margin-bottom:9px;font-size:10px;color:#999;padding:4px 8px}
.hero-form .btn{margin-top:20px;height:26px;border:1px solid #fff;color:#fff;font-size:10px;text-align:center;line-height:24px;text-transform:uppercase}
.arrow{width:20px;height:40px}

/* features */
.feature{width:220px;text-align:center}
.circle{width:130px;height:130px;margin:0 auto;border-radius:50%;border:6px solid #e5e5e5;background:#fff;display:flex;align-items:center;justify-content:center;font-size:15px;font-weight:600;text-transform:uppercase;color:#444;box-shadow:0 0 0 2px #cfcfcf inset}
.shelf{height:9px;background:var(--wood);margin:6px 10px 0;border-radius:2px;position:relative}
.shelf::before,.shelf::after{content:"";position:absolute;top:9px;width:10px;height:22px;background:var(--wood-dark)}
.shelf::before{left:28px}.shelf::after{right:28px}
.feature p{font-size:12px;line-height:19px;color:var(--muted);margin-top:40px}
.feature .more{display:block;margin-top:40px;font-size:13px;color:#333}

.rule{left:180px;width:840px;height:1px;background:var(--line)}
.section-title{left:0;width:1200px;text-align:center;font-size:20px;font-weight:600;text-transform:uppercase;color:#333}
.section-sub{left:0;width:1200px;text-align:center;font-size:11px;color:#999}

/* products */
.products{left:180px;top:980px;width:840px;display:flex;justify-content:space-between}
.product{width:126px;text-align:center}
.product .photo{height:180px}
.product .name{font-size:11px;color:#555;margin-top:10px}
.product .price{font-size:11px;color:#999;margin-top:4px}

/* featured */
.featured-photo{left:180px;top:1430px;width:300px;height:250px;background:linear-gradient(160deg,#efe6d8,#b38a5f 60%,#6e5238)}
.featured-body{left:510px;top:1418px;width:510px}
.featured-body h3{font-size:26px;font-weight:400;color:#333}
.meta{display:flex;justify-content:space-between;align-items:center;margin-top:22px;font-size:12px;color:#777}
.stars{color:var(--star);font-size:16px;letter-spacing:2px}
.meta .price{color:var(--wood);font-size:16px;font-weight:600}
.featured-body p{font-size:11px;line-height:18px;color:#777;margin-top:14px}
.share{display:flex;gap:10px;justify-content:flex-end;margin-top:16px}
.share span{width:10px;height:10px;border-radius:50%;background:#888}

/* testimonials */
.testimonial{width:400px;display:flex;gap:24px}
.avatar{flex:none;width:120px;height:120px;border-radius:50%;background:radial-gradient(circle,#e8d5c2,#b9a089)}
.testimonial p{font-size:11px;line-height:18px;color:#777;padding-top:10px}
.dots{left:0;width:1200px;top:2036px;display:flex;justify-content:center;gap:8px}
.dots span{width:10px;height:10px;border-radius:50%;background:#ccc}
.dots span.on{background:var(--wood)}

/* footer */
.footer{left:0;top:2120px;width:1200px;height:240px;background:var(--footer)}
.footer-bottom{left:0;top:2360px;width:1200px;height:68px;background:var(--footer-deep)}
.col-title{font-size:13px;font-weight:700;color:#fff;text-transform:uppercase}
.tweet{font-size:10px;line-height:16px;color:var(--footer-text);margin-top:14px;width:200px}
.tweet b{color:#fff;font-weight:600}
.gallery{display:grid;grid-template-columns:repeat(4,52px);gap:8px;margin-top:16px}
.gallery span{height:42px;border:2px solid #ddd;background:linear-gradient(135deg,#a58460,#5f4630)}
.gallery-intro{font-size:10px;line-height:15px;color:var(--footer-text);margin-top:12px;width:240px}
.input{width:230px;height:24px;background:#5d5d5d;margin-top:12px;font-size:10px;color:#aaa;padding:5px 8px}
.input.tall{height:60px}
.send{margin-top:12px;margin-left:180px;width:50px;height:22px;background:#222;color:#fff;font-size:10px;text-align:center;line-height:22px;text-transform:uppercase}
.copyright{left:180px;top:2388px;font-size:10px;color:#aaa}
.social{left:880px;top:2384px;display:flex;gap:14px}
.social span{width:14px;height:14px;border-radius:50%;background:#bbb}
</style>
</head>
<body>

<header>
  <div class="abs brand">
    <span class="brand-mark"></span>
    <div>
      <div class="brand-name">BRINDLEMOOR</div>
      <div class="brand-tag">Joinery with Spirit</div>
    </div>
  </div>
  <nav class="abs nav">
    <a href="#">Home</a><a href="#">Gallery</a><a href="#">Service</a><a href="#">About</a><a href="#">Contact</a>
  </nav>
  <div class="abs nav-shelf"></div>
</header>

<section class="hero">
  <div class="abs hero-frame"></div>
  <div class="abs hero-photo" role="img" aria-label="Bright modern kitchen with white cabinetry and a dining area"></div>
  <svg class="abs arrow" style="left:196px;top:268px" viewBox="0 0 20 40"><path d="M15 4 4 20l11 16" fill="none" stroke="#fff" stroke-width="3"/></svg>
  <svg class="abs arrow" style="left:1004px;top:268px" viewBox="0 0 20 40"><path d="M5 4l11 16L5 36" fill="none" stroke="#fff" stroke-width="3"/></svg>
  <form class="abs hero-form">
    <div class="field">Your Full Name</div>
    <div class="field">Your Email</div>
    <div class="field">Your Phone Number</div>
    <div class="field">Your Message</div>
    <div class="btn">Get a free quote</div>
  </form>
</section>

<section class="features">
  <div class="abs feature" style="left:170px;top:500px">
    <div class="circle">Product</div><div class="shelf"></div>
    <p>Our passion is to deliver inspired cabinetry solutions to suit all your needs, supported by our phenomenal star class customer service.</p>
    <a class="more">Read more</a>
  </div>
  <div class="abs feature" style="left:490px;top:500px">
    <div class="circle">Services</div><div class="shelf"></div>
    <p>Our passion is to deliver inspired cabinetry solutions to suit all your needs, supported by our phenomenal star class customer service.</p>
    <a class="more">Read more</a>
  </div>
  <div class="abs feature" style="left:810px;top:500px">
    <div class="circle">Mission</div><div class="shelf"></div>
    <p>Our passion is to deliver inspired cabinetry solutions to suit all your needs, supported by our phenomenal star class customer service.</p>
    <a class="more">Read more</a>
  </div>
</section>

<div class="abs rule" style="top:860px"></div>
<h2 class="abs section-title" style="top:888px">Some of our products</h2>
<div class="abs section-sub" style="top:922px">Handcrafted cabinets built to order for every room of the home</div>

<svg class="abs arrow" style="left:100px;top:1050px" viewBox="0 0 20 40"><path d="M15 4 4 20l11 16" fill="none" stroke="#444" stroke-width="3"/></svg>
<svg class="abs arrow" style="left:1080px;top:1050px" viewBox="0 0 20 40"><path d="M5 4l11 16L5 36" fill="none" stroke="#444" stroke-width="3"/></svg>
<div class="abs products">
  <div class="product"><div class="photo" role="img" aria-label="Dark wood display cabinet" style="background:linear-gradient(#3a2418,#1d120c)"></div><div class="name">Harbourline-Ambassador</div><div class="price">$398</div></div>
  <div class="product"><div class="photo" role="img" aria-label="Dark wood china hutch" style="background:linear-gradient(#4a2e1e,#24160e)"></div><div class="name">Harbourline-Ambassador</div><div class="price">$398</div></div>
  <div class="product"><div class="photo" role="img" aria-label="White storage cabinet" style="background:linear-gradient(#fbfbfb,#dcdcdc)"></div><div class="name">Harbourline-Ambassador</div><div class="price">$398</div></div>
  <div class="product"><div class="photo" role="img" aria-label="White low sideboard" style="background:linear-gradient(#f6f6f6,#d2d2d2)"></div><div class="name">Harbourline-Ambassador</div><div class="price">$398</div></div>
  <div class="product"><div class="photo" role="img" aria-label="Grey tall wardrobe" style="background:linear-gradient(#c9c9c9,#8c8c8c)"></div><div class="name">Harbourline-Ambassador</div><div class="price">$398</div></div>
  <div class="product"><div class="photo" role="img" aria-label="Light oak bookcase" style="background:linear-gradient(#d9a66c,#a06a34)"></div><div class="name">Harbourline-Ambassador</div><div class="price">$398</div></div>
</div>

<div class="abs rule" style="top:1270px"></div>
<h2 class="abs section-title" style="top:1290px">Featured product</h2>
<div class="abs section-sub" style="top:1324px">A closer look at one of our most requested kitchen designs</div>

<div class="abs featured-photo" role="img" aria-label="Warm wood kitchen with built-in ovens and a yellow accent wall"></div>
<article class="abs featured-body">
  <h3>Harbourline-Ambassador</h3>
  <div class="meta"><span><span class="stars">★★★★</span>&nbsp; Review: 4</span><span class="price">$ 398</span></div>
  <p>Solid maple doors, soft-close hinges and dovetail drawers come together in a kitchen built for daily cooking and long family dinners. Each box is cut, assembled and finished in our own shop, then fitted on site by our installation crew.</p>
  <p>Choose from painted, stained or natural finishes, and add pantry pull-outs, spice racks or a matching island. Every piece is measured to your room so nothing is wasted and every corner works hard for you.</p>
  <div class="share"><span></span><span></span><span></span><span></span></div>
</article>

<div class="abs rule" style="top:1760px"></div>
<h2 class="abs section-title" style="top:1778px">Testimonials</h2>
<div class="abs section-sub" style="top:1812px">What homeowners and contractors say about our work</div>

<div class="abs testimonial" style="left:180px;top:1860px">
  <div class="avatar" role="img" aria-label="Customer portrait"></div>
  <p>The crew turned our cramped kitchen into a bright, open space. Every drawer glides and the finish is flawless. Delivered on schedule and the install was spotless.</p>
</div>
<div class="abs testimonial" style="left:620px;top:1860px">
  <div class="avatar" role="img" aria-label="Customer portrait"></div>
  <p>We order cabinet boxes for most of our jobs now. Sizes are exact, parts arrive labelled and the team always answers the phone. Great partner for small contractors.</p>
</div>
<div class="abs dots"><span class="on"></span><span></span><span></span></div>

<footer>
  <div class="abs footer"></div>
  <div class="abs" style="left:180px;top:2150px">
    <div class="col-title">Latest tweets</div>
    <div class="tweet"><b>@brindlemoor</b> New walnut vanity install finished this week, photos in the gallery soon.</div>
    <div class="tweet"><b>@brindlemoor</b> Cabinet box orders now ship in ten days. Ask us for a trade quote today.</div>
  </div>
  <div class="abs" style="left:450px;top:2150px">
    <div class="col-title">Flicker gallery</div>
    <div class="gallery-intro">A look at recent kitchens, vanities and built-ins from our shop floor.</div>
    <div class="gallery"><span></span><span></span><span></span><span></span><span></span><span></span><span></span><span></span></div>
  </div>
  <div class="abs" style="left:780px;top:2150px">
    <div class="col-title">Contact us</div>
    <div class="input">Name</div>
    <div class="input">Email</div>
    <div class="input tall">Message</div>
    <div class="send">Send</div>
  </div>
  <div class="abs footer-bottom"></div>
  <div class="abs copyright">Copyright © www.brindlemoor.ca 2014</div>
  <div class="abs social"><span></span><span></span><span></span><span></span><span></span></div>
</footer>

</body>
</html>
```